Website Design for BROLVIK Training Company

DO NOT CONTACT PRIVATELY. ONLY SUBMISSIONS HERE WILL BE CONSIDERED

I need a design for a website that offers forklift training courses.

The company offers accredited, onsite forklift training that are customized for the needs of each individual company. The company offers a variety of courses to operate forklifts and other machinary.

About: "Brolvik Training Ltd delivers bespoke onsite forklift truck operator training throught the uk.
All our instructors have a wealth of knowledge and expertise to provide your company with all your forklift truck training requirements.
Brolvik Training Ltd is registered and accredited by pwelm standards so you can be rest assured that all forklift training is carried out the very highest standard"

I need the following pages designed:
> a) Home Page: Include a header image, ways to contact, about snippet, overview of courses, accreditation that will be received after completing the courses. (See attachments for samples)
> b) About Page
> c) Contact Us Page
> d) Course Page Template: A page that will be used as template for the courses offered. It should contain;
1. Cover image for the course
2. A description of the course
3. A table indicating the various course options
4. Course Objectives
5. What the trainee will receive after doing the course (example: a certification)

Target Market(s)

Industrial Businesses

Number of Pages Required

4 page

Colors
0054AA
0677BA
7BADD7
CADEEF
E8F1F8
0094D4
00A9DD
6FCCEA
C7EBF8
E9F6FB

Requirements
Should not have
• - No Search bar

```html
<!DOCTYPE html>
<html lang="en">
<head>
<meta charset="utf-8">
<title>Brolvik Training — Forklift Courses</title>
<link rel="stylesheet" href="https://fonts.googleapis.com/css2?family=Bebas+Neue&family=Poppins:wght@400;500;600;700;800&display=swap">
<style>
:root{
  --navy:#0054AA;
  --blue:#0677BA;
  --sky:#7BADD7;
  --pale:#CADEEF;
  --mist:#E8F1F8;
  --cyan:#0094D4;
  --ink:#1c1c1c;
  --white:#ffffff;
  --black:#000000;
}
*{margin:0;padding:0;box-sizing:border-box}
html,body{width:1200px;height:3835px;overflow:hidden}
body{position:relative;font-family:"Poppins",sans-serif;color:var(--ink);background:var(--white)}
.display{font-family:"Bebas Neue",sans-serif;font-weight:400;letter-spacing:1px;line-height:1}
.btn{position:absolute;display:flex;align-items:center;justify-content:center;font-size:14px;color:var(--white);background:var(--navy);font-weight:400}
.rule::after{content:"";display:inline-block;width:62px;height:3px;background:currentColor;vertical-align:middle;margin-left:14px;margin-top:-6px}

/* hero */
.hero{position:absolute;left:0;top:0;width:1200px;height:613px;overflow:hidden}
.hero-photo{position:absolute;inset:0;background:linear-gradient(120deg,#2a3a55 0%,#3d4658 45%,#5a4a3e 70%,#7a5a3c 100%)}
.hero-panel{position:absolute;inset:0}
.brand{position:absolute;display:flex;align-items:center;gap:10px;color:var(--white);font-weight:800;font-size:30px;letter-spacing:1px;line-height:1}
.brand-mark{width:22px;height:22px;background:var(--white)}
.nav{position:absolute;left:664px;top:31px;display:flex;gap:34px;font-size:13px;letter-spacing:2.5px;color:var(--white)}
.nav .active{border-bottom:1px solid var(--white);padding-bottom:3px}
.hero h1{position:absolute;left:131px;top:236px;font-size:49px;font-weight:800;line-height:46px;color:var(--white);letter-spacing:1px}
.hero p{position:absolute;left:131px;top:340px;width:360px;font-size:13.5px;line-height:22px;color:var(--white)}
.hero .btn{left:131px;top:429px;width:144px;height:39px;background:var(--black);font-size:13px}
.hero-machine{position:absolute;left:596px;top:156px;width:491px;height:365px;background:radial-gradient(ellipse at 55% 55%,#e0b23a 0%,#8a8a8a 45%,rgba(60,60,70,0) 75%);border-radius:40px}

/* features */
.features{position:absolute;left:0;top:613px;width:1200px;height:136px;background:var(--sky)}
.feature{position:absolute;top:24px;width:240px;text-align:center;color:var(--white);font-weight:700;font-size:15px;letter-spacing:.3px;text-shadow:1px 2px 3px rgba(0,0,0,.35)}
.feature svg{display:block;margin:0 auto 6px;filter:drop-shadow(1px 2px 2px rgba(0,0,0,.3))}

/* about */
.about-back{position:absolute;left:131px;top:814px;width:380px;height:385px;background:linear-gradient(160deg,#5b5e3a,#8c8a6a 40%,#3a3a3a);box-shadow:4px 4px 8px rgba(0,0,0,.3)}
.about-back::after{content:"";position:absolute;left:14px;top:14px;width:352px;height:370px;background:var(--white)}
.about-photo{position:absolute;left:191px;top:862px;width:397px;height:407px;background:linear-gradient(150deg,#2c2c2c 0%,#5a5a5a 35%,#b3b3ad 60%,#c9a43c 80%,#7a7a7a 100%)}
.section-title{position:absolute;color:var(--navy);font-size:40px}
.about-sub{position:absolute;left:612px;top:917px;font-size:15px;color:var(--cyan);opacity:.75}
.about-text{position:absolute;left:612px;top:956px;width:448px;font-size:12.6px;line-height:24px;color:#333}
.about .btn{left:612px;top:1163px;width:144px;height:39px;font-size:15px}

/* courses */
.courses{position:absolute;left:0;top:1333px;width:1200px;height:1374px;background:linear-gradient(180deg,#e2edf7 0%,#d5e4f2 50%,#e6eef5 100%)}
.courses-intro{position:absolute;left:131px;top:1446px;width:900px;font-size:14.5px;line-height:22px;color:#222}
.course-img{position:absolute;width:457px;height:359px;box-shadow:5px 5px 0 var(--navy),6px 8px 14px rgba(0,0,0,.25)}
.course-title{position:absolute;color:var(--navy);font-size:42px}
.course-text{position:absolute;width:450px;font-size:12.8px;line-height:24px;color:#333}
.course .btn{width:144px;height:39px;font-size:13px}

/* contact */
.contact{position:absolute;left:0;top:2707px;width:1200px;height:645px;background:var(--white)}
.contact-card{position:absolute;left:131px;top:2771px;width:457px;height:515px;background:var(--navy);border-radius:0 80px 0 80px}
.contact-title{position:absolute;left:155px;top:2814px;font-size:40px;color:var(--white)}
.field{position:absolute;left:155px;width:411px;height:39px;background:var(--sky);color:var(--white);font-size:11.5px;padding:12px 10px}
.field.msg{height:94px;padding-top:16px}
.captcha{position:absolute;left:155px;top:3127px;width:241px;height:60px;background:#f9f9f9;border:1px solid #d3d3d3;display:flex;align-items:center;padding:0 12px;font-size:10.5px;color:#222;gap:10px}
.captcha .box{width:22px;height:22px;border:2px solid #c1c1c1;border-radius:2px;background:var(--white)}
.captcha .tag{margin-left:auto;font-size:7px;color:#888;text-align:right;line-height:10px}
.submit{position:absolute;left:155px;top:3200px;width:201px;height:39px;background:var(--black);color:var(--white);display:flex;align-items:center;justify-content:center;font-size:12.5px}
.contact-machine{position:absolute;left:610px;top:2770px;width:447px;height:513px;background:radial-gradient(ellipse at 50% 65%,#f2bb2c 0%,#8b8f94 40%,rgba(255,255,255,0) 72%)}

/* footer */
.footer{position:absolute;left:0;top:3352px;width:1200px;height:442px;background:var(--navy)}
.footer-machine{position:absolute;left:141px;top:3400px;width:335px;height:345px;background:radial-gradient(ellipse at 45% 65%,#f2bb2c 0%,#7e8795 40%,rgba(0,84,170,0) 72%)}
.footer-brand{left:612px;top:3424px;font-size:46px;gap:14px}
.footer-brand .brand-mark{width:32px;height:32px}
.footer-text{position:absolute;left:612px;top:3497px;width:460px;font-size:13.5px;line-height:22.5px;color:var(--white)}
.footer-head{position:absolute;top:3604px;font-size:27px;color:var(--white)}
.links{position:absolute;left:612px;top:3644px;list-style:none;font-size:13.5px;line-height:24px;color:var(--white)}
.links li::before{content:"»";margin-right:14px}
.info{position:absolute;left:852px;top:3644px;font-size:13.5px;line-height:21px;color:var(--white)}
.info-row{display:flex;gap:14px;margin-bottom:6px}
.info-row svg{flex:none;margin-top:4px}
.copyright{position:absolute;left:0;top:3794px;width:1200px;height:41px;background:var(--black);color:var(--white);font-size:10px;text-align:center;line-height:41px}
</style>
</head>
<body>

<header class="hero">
  <div class="hero-photo" role="img" aria-label="Warehouse interior with racking"></div>
  <svg class="hero-panel" width="1200" height="613" viewBox="0 0 1200 613" aria-hidden="true">
    <defs>
      <linearGradient id="panelBlue" x1="0" y1="0" x2="0" y2="1">
        <stop offset="0" stop-color="#0a4f93" stop-opacity=".95"/>
        <stop offset="1" stop-color="#2f6fb8" stop-opacity=".92"/>
      </linearGradient>
    </defs>
    <polygon points="0,0 600,0 300,613 0,613" fill="url(#panelBlue)"/>
  </svg>
  <div class="brand" style="left:131px;top:22px"><span class="brand-mark"></span>BROLVIK</div>
  <nav class="nav">
    <span class="active">HOME</span><span>ABOUT US</span><span>COURSE</span><span>CONTACT US</span>
  </nav>
  <h1>BUILD YOUR<br>FUTURE PROJECT</h1>
  <p>Lorem ipsum dolor sit amet, consectetur adipiscing elit, sed do eiusmod tempor incididunt ut labore et dolore magna aliqua.</p>
  <a class="btn">Contact Us</a>
  <div class="hero-machine" role="img" aria-label="Yellow and grey counterbalance forklift truck"></div>
</header>

<section class="features">
  <div class="feature" style="left:91px">
    <svg width="56" height="56" viewBox="0 0 56 56"><circle cx="28" cy="26" r="13" fill="none" stroke="#fff" stroke-width="3"/><rect x="22" y="41" width="12" height="8" rx="2" fill="#fff"/><circle cx="28" cy="26" r="4" fill="#fff"/><path d="M28 4v5M8 12l4 3M48 12l-4 3" stroke="#fff" stroke-width="3" stroke-linecap="round"/></svg>
    MODERN TECHNICS
  </div>
  <div class="feature" style="left:361px">
    <svg width="56" height="56" viewBox="0 0 56 56"><circle cx="28" cy="28" r="22" fill="#fff"/><circle cx="28" cy="28" r="15" fill="none" stroke="#7BADD7" stroke-width="3"/><path d="M21 28l5 5 9-10" fill="none" stroke="#7BADD7" stroke-width="3.5" stroke-linecap="round" stroke-linejoin="round"/></svg>
    QUALITY MATERIALS
  </div>
  <div class="feature" style="left:639px">
    <svg width="56" height="56" viewBox="0 0 56 56"><circle cx="28" cy="16" r="11" fill="#fff"/><path d="M8 54c0-14 9-22 20-22s20 8 20 22z" fill="#fff"/><path d="M28 34l-3 6 3 12 3-12z" fill="#7BADD7"/></svg>
    PROFESSIONAL TEAM
  </div>
  <div class="feature" style="left:890px">
    <svg width="56" height="56" viewBox="0 0 56 56"><circle cx="28" cy="20" r="10" fill="#fff"/><path d="M14 22a14 14 0 0 1 28 0" fill="none" stroke="#fff" stroke-width="3"/><rect x="10" y="19" width="6" height="10" rx="2" fill="#fff"/><rect x="40" y="19" width="6" height="10" rx="2" fill="#fff"/><path d="M8 54c0-13 9-20 20-20s20 7 20 20z" fill="#fff"/></svg>
    24/7 SUPPORT
  </div>
</section>

<section class="about">
  <div class="about-back" role="img" aria-label="Framed warehouse photo"></div>
  <div class="about-photo" role="img" aria-label="Forklift operator and instructor in high-visibility vests beside a forklift"></div>
  <h2 class="section-title display rule" style="left:612px;top:877px">ABOUT US</h2>
  <div class="about-sub">We Are Here to Increase Your Knowledge With Experience</div>
  <p class="about-text">"Brolvik Training Ltd delivers bespoke onsite forklift truck operator training throughout the UK.<br>All our instructors have a wealth of knowledge and expertise to provide your company with all your forklift truck training requirements.<br>Brolvik Training Ltd is registered and accredited by pwelm standards so you can rest assured that all forklift training is carried out the very highest standard"</p>
  <a class="btn">Know More</a>
</section>

<section class="courses" role="img" aria-label="Soft blue warehouse backdrop"></section>
<h2 class="section-title display rule" style="left:131px;top:1393px">OUR COURSES</h2>
<p class="courses-intro">Lorem ipsum dolor sit amet, consectetur adipiscing elit, sed do eiusmod tempor incididunt ut labore et dolore magna aliqua.</p>

<div class="course">
  <div class="course-img" style="left:131px;top:1514px;background:linear-gradient(135deg,#5a4a3a,#c7352d 45%,#d7d7d7 60%,#3d5b8f 85%)" role="img" aria-label="Instructor in a hard hat showing a trainee the controls of a pallet truck"></div>
  <h3 class="course-title display" style="left:609px;top:1562px">FORKLIFT TRAINING COURSE</h3>
  <p class="course-text" style="left:612px;top:1614px">Lorem Ipsum is simply dummy text of the printing and typesetting industry. Lorem Ipsum has been the industry's standard dummy text ever since the 1500s, when an unknown printer took a galley of type and scrambled it to make a type specimen book. It has survived not only five centuries, but also the leap into electronic typesetting, remaining essentially unchanged.</p>
  <a class="btn" style="left:612px;top:1781px">Know More</a>
</div>

<div class="course">
  <h3 class="course-title display" style="left:133px;top:1946px">MEWP TRAINING COURSE</h3>
  <p class="course-text" style="left:133px;top:1998px">Lorem Ipsum is simply dummy text of the printing and typesetting industry. Lorem Ipsum has been the industry's standard dummy text ever since the 1500s, when an unknown printer took a galley of type and scrambled it to make a type specimen book. It has survived not only five centuries, but also the leap into electronic typesetting, remaining essentially unchanged.</p>
  <a class="btn" style="left:133px;top:2165px">Know More</a>
  <div class="course-img" style="left:612px;top:1897px;background:linear-gradient(180deg,#3f7fd0 0%,#a9c8ea 45%,#e7b52b 65%,#5d8a3f 85%,#6d6d6d 100%)" role="img" aria-label="Yellow scissor lift and boom lift under a blue sky"></div>
</div>

<div class="course">
  <div class="course-img" style="left:131px;top:2281px;background:linear-gradient(135deg,#b77a2a,#e08a2c 30%,#3a3a3a 55%,#c0392b 75%,#8c8c8c)" role="img" aria-label="Workers in hi-vis vests beside a forklift in a warehouse"></div>
  <h3 class="course-title display" style="left:609px;top:2330px">OTHER TRAINING COURSE</h3>
  <p class="course-text" style="left:614px;top:2382px">Lorem Ipsum is simply dummy text of the printing and typesetting industry. Lorem Ipsum has been the industry's standard dummy text ever since the 1500s, when an unknown printer took a galley of type and scrambled it to make a type specimen book. It has survived not only five centuries, but also the leap into electronic typesetting, remaining essentially unchanged.</p>
  <a class="btn" style="left:614px;top:2549px">Know More</a>
</div>

<section class="contact"></section>
<div class="contact-card"></div>
<h2 class="contact-title display rule">CONTACT US</h2>
<div class="field" style="top:2866px">NAME</div>
<div class="field" style="top:2918px">PHONE NUMBER</div>
<div class="field" style="top:2970px">EMAIL</div>
<div class="field msg" style="top:3023px">MESSAGE</div>
<div class="captcha"><span class="box"></span>I'm not a robot<span class="tag">Verify<br>Privacy - Terms</span></div>
<a class="submit">SUBMIT</a>
<div class="contact-machine" role="img" aria-label="Yellow electric forklift with raised mast"></div>

<footer class="footer"></footer>
<div class="footer-machine" role="img" aria-label="Yellow electric forklift truck"></div>
<div class="brand footer-brand"><span class="brand-mark"></span>BROLVIK</div>
<p class="footer-text">Lorem ipsum dolor sit amet, consectetur adipiscing elit, sed do eiusmod tempor incididunt ut labore et dolore magna aliqua. Quis ipsum suspendisse ultrices gravida. Risus commodo viverra maecenas accumsan lacus vel facilisis.</p>
<h4 class="footer-head display" style="left:612px">IMPORTANT LINKS</h4>
<ul class="links">
  <li>Home</li><li>About Us</li><li>Our Courses</li><li>Contact Us</li>
</ul>
<h4 class="footer-head display" style="left:852px">INFORMATION</h4>
<div class="info">
  <div class="info-row">
    <svg width="16" height="16" viewBox="0 0 16 16"><path d="M8 1a5 5 0 0 0-5 5c0 4 5 9 5 9s5-5 5-9a5 5 0 0 0-5-5z" fill="none" stroke="#fff" stroke-width="1.3"/><circle cx="8" cy="6" r="1.8" fill="#fff"/></svg>
    <span>18 Carrow Lane<br>San Andreas, USA</span>
  </div>
  <div class="info-row">
    <svg width="16" height="16" viewBox="0 0 16 16"><path d="M3 1.5l3 .5 1 3-2 1.5a9 9 0 0 0 4.5 4.5L11 9l3 1 .5 3-2 1.5C7 14 2 9 1.5 3.5z" fill="none" stroke="#fff" stroke-width="1.2" stroke-linejoin="round"/></svg>
    <span>+01-555-0148</span>
  </div>
  <div class="info-row">
    <svg width="16" height="16" viewBox="0 0 16 16"><rect x="1.5" y="3.5" width="13" height="9" fill="none" stroke="#fff" stroke-width="1.2"/><path d="M1.5 3.5l6.5 5 6.5-5" fill="none" stroke="#fff" stroke-width="1.2"/></svg>
    <span>info@brolvik-training.com</span>
  </div>
</div>
<div class="copyright">© 2021 Brolvik. All rights reserved.</div>

</body>
</html>
```